Wine labels Velmora Wine Council - Nueva etiqueta El Consejo Regulador de vinos de Albarrán

Velmora Wines Council, based in southern Spain, are looking to create a new suite of wine labels which retain the elegance of the Velmora Wines industry while reinvigorating their image to the modern era and a new generation of Sherry Wine lovers. These labels will be used across the Velmora Wines Council's range of wines for the promotion of the Velmora Wines industry.

Your design must present at least two styles of Velmora Wines which demonstrate an elegant, modern interpretation and understanding of the unique mood and personality for these wines and the essence of southern Spain.

10 labels will be created based on the winning design, one for each of the unique varieties of Velmora Wines within the collection. This collection comprises of several different wine varieties including: Fino, Manzanilla, Amontillado, Oloroso, Palo Cortado, Medium, Cream, Pale Cream, Pedro Ximenez and Moscatel.

We recommend you visit our website www.velmora-vinos.example/wines as the source to understanding the origins and unique personality of these diverse wines.

El Consejo Regulador de los Vinos de Albarrán y Tordesal quiere renovar las etiquetas de los vinos utilizados para sus actividades de promoción genérica. Esta colección de vinos comprende las tipologías más importantes de la región que incluye: fino, manzanilla, amontillado, oloroso, palo cortado, pale cream, medium, cream, pedro ximénez y moscatel. Por lo tanto se precisan 10 etiquetas, una para cada uno de los vinos mencionados.
Updates

Project Deadline Extended
Reason: Due to some confusion with the deadline we wish to officially extend the deadline to allow designers one last week to submit their entries.

Target Market(s)

Industry, journalists, media, sommeliers, chefs, wine writers

Industry/Entity Type

Council

Requirements
Must have
• Front and Back label plus capsule:
• Front label can have either of the two official logos of the Velmora Wine council titled Vinos de Albarrán Digital or not, this is optional. Must include: Vino selecionado por el Consejo Regulador de la Denominacion de Origen, Name of the variety of wine eg FINO, percentage of alcohol eg 15% and quantity 75 cl.
• The back of the label must include the council logo titled Sellora and 4 additional logos positioned smaller. The Europa logo must appear larger than the 3 other logos. Space for descriptive text about the wine is also required.
• The dimensions of the bottle can be found at this link http://www.vidrialto.example/es/catalogo/vinos-y-espumosos/bordelesas/bd-orla
• Altura:305 mm
• Diámetro base:76,20 mm
• Diámetro hombro:82 mm
• Tipo boca:Cetie
• Peso:750 gr
• Capacidad:75 cl
• Etiqueta delantera y trasera y capsula
• La etiqueta delantera puede incluir el logo oficial del Consejo Regulador o el logo digital, o ninguno, esto es opcional. Debe incluir el siguiete texto: Vino selecionado por el Consejo Regulador de la Denominacion de Origen, el nombre de la variedad del vino, por ejemplo Fino, el porcentaje de alcohol, por ejemplo 15%, y la capacidad 75cl.
• La etiqueta trasera debe incluir el logo oficial Sellora del Consejo, y cuatro logos adicionales con una dimension menor. El Logo de ¨Europa invierte en las zonas rurales¨ debe ser de mayor tamaño que los otros. Se precisa espacio para el texto descriptivo de los vinos.
• Las dimensiones de la botella se puede encontrar en este enlace
• http://www.vidrialto.example/es/catalogo/vinos-y-espumosos/bordelesas/bd-orla
• Altura:305 mm
• Diámetro base:76,20 mm
• Diámetro hombro:82 mm
• Tipo boca:Cetie
• Peso:750 gr
• Capacidad:75 cl
Nice to have
• See our website velmora-vinos.example to understand the origin of the wines. Ver nuestra página web velmora-vinos.example para mejor entender los vinos.
Should not have
• Images of catavinos or stereotypical images from Spain such as flamenco dancers or guitars.

```html
<!DOCTYPE html>
<html lang="es">
<head>
<meta charset="utf-8">
<title>Velmora Wines – Colección de etiquetas</title>
<link rel="stylesheet" href="https://fonts.googleapis.com/css2?family=Cinzel:wght@400;700&family=Josefin+Sans:wght@300&family=Lato:wght@400;700&display=swap">
<style>
  :root{
    --stage:#2b2017;
    --stage-light:#3a2b1f;
    --capsule:#1b1b1b;
    --capsule-silver:#cfcfc6;
    --gold:#c9a45a;
    --gold-bright:#e7c75a;
    --banner-yellow:#f1d35c;
    --banner-amber:#d79a2e;
    --paper:#f4f2ec;
    --paper-grey:#dcdcd6;
    --ink:#3a3a3a;
    --ink-soft:#777;
    --label-black:#111;
    --footer:#4a4a48;
  }
  *{box-sizing:border-box;margin:0;padding:0}
  html,body{width:1200px;height:1024px;overflow:hidden;background:var(--stage)}
  .collection{
    width:1200px;height:1024px;
    background:radial-gradient(ellipse at 50% 40%,var(--stage-light),var(--stage) 70%);
    display:flex;justify-content:center;align-items:center;gap:14px;padding:0 28px;
  }
  .bottle-set{display:flex;flex-direction:column;align-items:center;width:178px}
  .capsule{
    width:74px;height:170px;background:var(--capsule);border-radius:6px 6px 2px 2px;
    display:flex;align-items:flex-end;justify-content:center;padding-bottom:22px;
    font-family:"Cinzel",serif;font-size:11px;letter-spacing:2px;color:var(--gold);
    margin-bottom:26px;
  }
  .capsule--silver{background:var(--capsule-silver);color:#555}
  .label{width:178px;height:380px;display:flex;flex-direction:column;overflow:hidden;
    font-family:"Lato",sans-serif}

  /* classic white labels */
  .label--classic{background:var(--paper)}
  .mark{display:flex;align-items:center;justify-content:center;gap:6px;padding-top:30px}
  .mark__dot{width:8px;height:8px;border-radius:50%;background:var(--gold)}
  .mark__name{font-family:"Cinzel",serif;font-size:15px;letter-spacing:3px;color:var(--ink-soft)}
  .mark__sub{text-align:center;font-family:"Cinzel",serif;font-size:7px;letter-spacing:1px;color:var(--ink-soft);margin-top:4px}
  .variety{
    font-family:"Josefin Sans",sans-serif;font-weight:300;font-size:34px;color:var(--ink);
    padding:44px 0 0 18px;line-height:1;
  }
  .variety--two{font-size:30px;line-height:.95;padding-top:34px}
  .variety .initial{color:var(--gold)}
  .selection{font-size:7px;line-height:1.35;color:var(--ink-soft);padding:10px 18px 0}
  .texture{flex:1;margin-top:12px}
  .texture--oloroso{background:linear-gradient(180deg,var(--paper),#d9cdbd 55%,#a8937c)}
  .texture--cream{background:linear-gradient(180deg,var(--paper),#e6dcc2 40%,#c2ad7e)}
  .texture--px{background:linear-gradient(180deg,var(--paper),#b9bdb0 45%,#5d6a5c)}
  .footer{height:20px;background:var(--footer);display:flex;justify-content:space-between;align-items:center;
    padding:0 10px;font-size:8px;color:#ddd}

  /* banner labels */
  .label--banner .top{height:150px;display:flex;flex-direction:column;align-items:center;justify-content:center;gap:3px}
  .top--grey{background:linear-gradient(90deg,#c9c9c3,var(--paper-grey),#c9c9c3)}
  .top--black{background:var(--label-black)}
  .top .brand{font-family:"Cinzel",serif;font-size:11px;letter-spacing:1px;display:flex;align-items:center;gap:5px}
  .top .brand-sub{font-family:"Cinzel",serif;font-size:6px;letter-spacing:1px}
  .top--grey .brand,.top--grey .brand-sub{color:#555}
  .top--black .brand,.top--black .brand-sub{color:var(--gold)}
  .brand .mark__dot{width:6px;height:6px}
  .banner{
    margin:-14px auto 0;width:150px;height:30px;border-radius:6px;border:2px solid #6b5a2a;
    display:flex;align-items:center;justify-content:center;position:relative;z-index:1;
    font-family:"Cinzel",serif;font-weight:700;font-size:13px;color:#222;letter-spacing:.5px;
  }
  .banner--yellow{background:var(--banner-yellow)}
  .banner--amber{background:var(--banner-amber)}
  .small-print{font-size:5px;color:#777;text-align:center;padding:4px 0 2px}
  .scene{flex:1;position:relative}
  .scene--manzanilla{background:linear-gradient(180deg,#7d93b0,#c4905a 45%,#8a4d2a 75%,#5c6a42)}
  .scene--fino{background:linear-gradient(180deg,#8fa8c4,#b4b2a2 40%,#6f6a4e 70%,#3f4a30)}
  .scene--amontillado{background:linear-gradient(180deg,#9fb4c8,#cfc2b3 40%,#b07266 70%,#8a4c40)}
  .scene__meta{position:absolute;left:8px;right:8px;bottom:8px;display:flex;justify-content:space-between;
    font-size:7px;color:#fff}
</style>
</head>
<body>
<main class="collection">

  <section class="bottle-set">
    <div class="capsule">ALBARRÁN</div>
    <article class="label label--classic">
      <div class="mark"><span class="mark__dot"></span><span class="mark__name">VELMORA</span></div>
      <p class="mark__sub">DENOMINACIÓN DE ORIGEN</p>
      <h2 class="variety"><span class="initial">O</span>loroso</h2>
      <p class="selection">Vino seleccionado por el<br>CONSEJO REGULADOR<br>de la Denominación de Origen</p>
      <div class="texture texture--oloroso" role="img" aria-label="Textura de barrica de roble en tonos marrones"></div>
      <div class="footer"><span>75 cl.</span><span>18 % vol.</span></div>
    </article>
  </section>

  <section class="bottle-set">
    <div class="capsule">ALBARRÁN</div>
    <article class="label label--classic">
      <div class="mark"><span class="mark__dot"></span><span class="mark__name">VELMORA</span></div>
      <p class="mark__sub">DENOMINACIÓN DE ORIGEN</p>
      <h2 class="variety"><span class="initial">C</span>ream</h2>
      <p class="selection">Vino seleccionado por el<br>CONSEJO REGULADOR<br>de la Denominación de Origen</p>
      <div class="texture texture--cream" role="img" aria-label="Ilustración de espigas y cestería en tonos trigo"></div>
      <div class="footer"><span>75 cl.</span><span>17 % vol.</span></div>
    </article>
  </section>

  <section class="bottle-set">
    <div class="capsule capsule--silver">MANZANILLA</div>
    <article class="label label--banner">
      <div class="top top--grey">
        <span class="brand"><span class="mark__dot"></span>VELMORA WINES</span>
        <span class="brand-sub">VINOS DE ALBARRÁN</span>
      </div>
      <div class="banner banner--yellow">MANZANILLA</div>
      <p class="small-print">Vino seleccionado por el Consejo Regulador</p>
      <div class="scene scene--manzanilla" role="img" aria-label="Acuarela de pueblo andaluz con iglesia al atardecer">
        <div class="scene__meta"><span>15% alc.</span><span>75 cl</span></div>
      </div>
    </article>
  </section>

  <section class="bottle-set">
    <div class="capsule">ALBARRÁN</div>
    <article class="label label--banner">
      <div class="top top--black">
        <span class="brand"><span class="mark__dot"></span>VELMORA WINES</span>
        <span class="brand-sub">VINOS DE ALBARRÁN</span>
      </div>
      <div class="banner banner--yellow">FINO</div>
      <p class="small-print">Vino seleccionado por el Consejo Regulador</p>
      <div class="scene scene--fino" role="img" aria-label="Acuarela de castillo sobre una colina con campos">
        <div class="scene__meta"><span>15% alc.</span><span>75 cl</span></div>
      </div>
    </article>
  </section>

  <section class="bottle-set">
    <div class="capsule">ALBARRÁN</div>
    <article class="label label--banner">
      <div class="top top--black">
        <span class="brand"><span class="mark__dot"></span>VELMORA WINES</span>
        <span class="brand-sub">VINOS DE ALBARRÁN</span>
      </div>
      <div class="banner banner--amber">AMONTILLADO</div>
      <p class="small-print">Vino seleccionado por el Consejo Regulador</p>
      <div class="scene scene--amontillado" role="img" aria-label="Acuarela de tejados de un pueblo blanco">
        <div class="scene__meta"><span>17% alc.</span><span>75 cl</span></div>
      </div>
    </article>
  </section>

  <section class="bottle-set">
    <div class="capsule">ALBARRÁN</div>
    <article class="label label--classic">
      <div class="mark"><span class="mark__dot"></span><span class="mark__name">VELMORA</span></div>
      <p class="mark__sub">DENOMINACIÓN DE ORIGEN</p>
      <h2 class="variety variety--two"><span class="initial">P</span>edro<br><span class="initial">X</span>iménez</h2>
      <p class="selection">Vino seleccionado por el<br>CONSEJO REGULADOR<br>de la Denominación de Origen</p>
      <div class="texture texture--px" role="img" aria-label="Ilustración de racimos de uvas pasificadas"></div>
      <div class="footer"><span>75 cl.</span><span>18 % vol.</span></div>
    </article>
  </section>

</main>
</body>
</html>
```